Harborline Trailer Leasing

We need a website for our new Trailer leasing company.
Check out https://oakridgetrailerleasing.example/home for ideas.

Coding

Coded - Design and coding required

Number of Pages Required

4 page

```html
<!DOCTYPE html>
<html lang="en">
<head>
<meta charset="utf-8">
<title>Harborline Trailer Leasing</title>
<link href="https://fonts.googleapis.com/css2?family=Roboto:wght@400;500;700&family=Rubik:wght@600;700&display=swap" rel="stylesheet">
<style>
:root{
  --navy:#1b4f93;
  --navy-dark:#163f78;
  --slate:#6b82a0;
  --slate-light:#8d9db3;
  --ink:#1d1d1d;
  --muted:#6b6b6b;
  --white:#ffffff;
}
*{box-sizing:border-box;margin:0;padding:0}
html,body{width:1200px;height:3105px;overflow:hidden}
body{position:relative;font-family:'Roboto',sans-serif;color:var(--ink);background:var(--white)}
.abs{position:absolute}
.heading{font-family:'Rubik',sans-serif;font-weight:700;text-transform:uppercase;letter-spacing:.3px}

/* top bar + header */
.topbar{left:0;top:0;width:1200px;height:37px}
.topbar-links{top:10px;font-size:14px;color:var(--white)}
.topbar-links span{margin:0 10px}
.brand{font-family:'Roboto',sans-serif;font-weight:700;color:var(--navy);font-size:30px;display:flex;align-items:center;gap:10px}
.brand-dot{width:26px;height:26px;border-radius:50%;background:var(--navy)}
.nav{top:62px;left:478px;width:640px;font-size:16px;font-weight:500}
.nav a{position:absolute;color:var(--ink);text-decoration:none;white-space:nowrap}

/* hero */
.hero-title{left:108px;top:306px;font-size:43px;line-height:50px;color:var(--white)}
.hero-sub{left:111px;top:423px;width:500px;font-size:18px;line-height:28px;color:var(--white);font-weight:500}
.hero-cta{left:820px;top:573px;width:332px;text-align:center;color:var(--white);font-family:'Roboto',sans-serif;font-weight:500;font-size:36px;line-height:41px}
.btn{display:flex;align-items:center;justify-content:center;gap:8px;background:var(--navy);color:var(--white);font-weight:700;border-radius:30px;text-transform:uppercase;font-size:15px}

/* why */
.why-title{left:669px;top:952px;font-size:38px;color:var(--slate)}
.why-title b{color:var(--navy);font-weight:700}
.feature{left:669px;width:430px}
.feature-icon{position:absolute;left:0;top:0;width:77px;height:77px;border-radius:50%;background:var(--white);box-shadow:0 3px 12px rgba(0,0,0,.13);display:flex;align-items:center;justify-content:center}
.feature-icon.active{background:var(--navy)}
.feature h3{position:absolute;left:102px;top:0;font-size:18px;font-weight:500;white-space:nowrap}
.feature p{position:absolute;left:102px;top:31px;width:330px;font-size:14.5px;line-height:23.5px;color:var(--muted)}

/* welcome */
.welcome-title{left:0;top:1638px;width:1200px;text-align:center;font-size:38px;color:var(--white)}
.card{top:1740px;width:308px;height:402px;background:var(--white);border-radius:12px;text-align:center}
.card-photo{position:absolute;left:7px;top:7px;width:294px;height:197px}
.card-icon{position:absolute;left:118px;top:168px;width:72px;height:72px;border-radius:50%;background:var(--slate);border:4px solid var(--white);display:flex;align-items:center;justify-content:center}
.card h3{position:absolute;left:0;width:100%;font-size:19px;font-weight:500}
.card p{position:absolute;left:20px;width:268px;font-size:14px;line-height:22px;color:var(--muted)}
.card .btn{position:absolute;height:37px;font-size:14px}

/* info */
.info-title{left:108px;top:2318px;font-size:39px;line-height:38px;color:var(--white)}
.info-sub{left:113px;top:2407px;width:460px;font-size:15px;line-height:24px;color:var(--white)}
.field{height:40px;width:223px;background:var(--white);font-size:12px;color:#777;padding:13px 12px}

/* footer */
.foot-h{font-size:17px;font-weight:500;color:var(--slate)}
.foot-label{font-size:12px;font-weight:700;color:var(--slate)}
.foot-text{font-size:14px;color:#444;line-height:19px}
.foot-links{font-size:14px;color:#555;line-height:26px}
.social{width:32px;height:32px;border-radius:50%;border:1px solid #777}
.legal{top:3062px;font-size:14px;color:#555}
</style>
</head>
<body>

<!-- top bar -->
<svg class="abs topbar" viewBox="0 0 1200 37" aria-hidden="true"><path d="M438 0H1200V37H478Z" fill="var(--navy)"/></svg>
<div class="abs topbar-links" style="left:509px">
  <svg width="11" height="12" viewBox="0 0 11 12" style="vertical-align:-1px"><circle cx="5.5" cy="3.2" r="3" fill="#fff"/><path d="M0 12c0-4 2.5-6 5.5-6s5.5 2 5.5 6z" fill="#fff"/></svg> Apply for Account<span>|</span><svg width="8" height="12" viewBox="0 0 8 12" style="vertical-align:-1px"><path d="M4 0a4 4 0 0 1 4 4c0 3-4 8-4 8S0 7 0 4a4 4 0 0 1 4-4z" fill="#fff"/></svg> Find Locations
</div>
<div class="abs topbar-links" style="left:978px">Login<span>|</span>Register</div>

<div class="abs brand" style="left:111px;top:38px"><span class="brand-dot"></span>Harborline</div>

<nav class="abs nav">
  <a style="left:0">Home</a>
  <a style="left:69px">Rent/Lease</a>
  <a style="left:174px">Trailers</a>
  <a style="left:249px">Services</a>
  <a style="left:327px">Company</a>
  <a style="left:411px">Careers</a>
  <a style="left:492px">Contact Us</a>
  <svg class="abs" style="left:595px;top:3px" width="14" height="14" viewBox="0 0 14 14"><circle cx="6" cy="6" r="4.5" fill="none" stroke="#1d1d1d" stroke-width="2"/><path d="M9.5 9.5L13 13" stroke="#1d1d1d" stroke-width="2.2"/></svg>
</nav>

<!-- hero -->
<svg class="abs" style="left:0;top:106px" width="1200" height="760" viewBox="0 106 1200 760" role="img" aria-label="Photo of a red semi truck hauling a leasing trailer along a highway at dusk">
  <defs>
    <linearGradient id="heroSky" x1="0" y1="0" x2="0" y2="1">
      <stop offset="0" stop-color="#3c5a78"/>
      <stop offset=".35" stop-color="#7f8f96"/>
      <stop offset=".55" stop-color="#565a4c"/>
      <stop offset="1" stop-color="#4a4b48"/>
    </linearGradient>
    <linearGradient id="heroTruck" x1="0" y1="0" x2="1" y2="0">
      <stop offset="0" stop-color="#7d8590" stop-opacity="0"/>
      <stop offset=".5" stop-color="#8a2a2a" stop-opacity=".35"/>
      <stop offset="1" stop-color="#9c2525" stop-opacity=".55"/>
    </linearGradient>
  </defs>
  <path d="M0 652 Q520 930 1200 470 V535 Q560 960 0 660Z" fill="var(--navy)"/>
  <path d="M0 106H1200V450 Q520 900 0 648Z" fill="url(#heroSky)"/>
  <path d="M600 250 L1200 200 V450 Q960 610 700 650 L600 480Z" fill="url(#heroTruck)"/>
  <circle cx="986" cy="670" r="183" fill="var(--slate-light)"/>
  <circle cx="986" cy="670" r="160" fill="var(--slate)"/>
</svg>

<h1 class="abs heading hero-title">Making trailer leasing<br>affordable and easy</h1>
<p class="abs hero-sub">Harborline Trailer Leasing was founded in 2005 with a vision to make a difference in the trailer leasing industry</p>
<div class="abs hero-cta">Ready for a new lease on trailer leasing?</div>
<a class="abs btn" style="left:876px;top:723px;width:218px;height:48px;font-size:16px">Let’s get started
  <svg width="16" height="16" viewBox="0 0 16 16"><circle cx="8" cy="8" r="8" fill="#fff"/><path d="M6.5 4.5L10 8l-3.5 3.5" stroke="var(--navy)" stroke-width="2.2" fill="none"/></svg>
</a>

<!-- why choose us -->
<svg class="abs" style="left:75px;top:940px" width="550" height="450" viewBox="0 0 550 450" role="img" aria-label="Photo of a white leasing trailer on a tree-lined highway">
  <defs>
    <linearGradient id="whyPhoto" x1="0" y1="0" x2="1" y2="1">
      <stop offset="0" stop-color="#2f4a28"/>
      <stop offset=".45" stop-color="#d5d9dc"/>
      <stop offset=".7" stop-color="#7a8a6a"/>
      <stop offset="1" stop-color="#4f7a2e"/>
    </linearGradient>
  </defs>
  <path d="M0 430 L70 160 Q140 20 410 0 H548 Q480 300 300 448 L0 430Z" fill="url(#whyPhoto)"/>
  <path d="M180 448 Q50 300 120 200 Q200 80 470 0" fill="none" stroke="#fff" stroke-width="20"/>
  <path d="M295 448 Q170 330 190 230 Q220 110 480 8" fill="none" stroke="#fff" stroke-width="16"/>
</svg>

<h2 class="abs heading why-title"><b>Why</b> choose us?</h2>

<div class="abs feature" style="top:1033px;height:110px">
  <div class="feature-icon active"><svg width="34" height="38" viewBox="0 0 34 38"><rect x="4" y="2" width="22" height="32" rx="2" fill="none" stroke="#fff" stroke-width="2"/><path d="M9 12h12M9 18h12M9 24h8" stroke="#fff" stroke-width="2"/></svg></div>
  <h3>Flexible Lease/Rent Terms</h3>
  <p>Harborline Trailer Leasing is covering more ground than ever before. With new locations across the country, you’ll get greater efficiency</p>
</div>
<div class="abs feature" style="top:1157px;height:110px">
  <div class="feature-icon"><svg width="36" height="36" viewBox="0 0 36 36"><circle cx="18" cy="18" r="9" fill="none" stroke="var(--navy)" stroke-width="2"/><circle cx="18" cy="18" r="3.5" fill="none" stroke="var(--navy)" stroke-width="2"/><path d="M18 4v5M18 27v5M4 18h5M27 18h5M8 8l3.5 3.5M24.5 24.5L28 28M8 28l3.5-3.5M24.5 11.5L28 8" stroke="var(--navy)" stroke-width="2"/></svg></div>
  <h3>Innovative Technology</h3>
  <p>We offer real-time GPS tracking plus geofencing on all leases and rentals. And all Harborline reefers come standard with refrigeration monitoring.</p>
</div>
<div class="abs feature" style="top:1278px;height:110px">
  <div class="feature-icon"><svg width="34" height="36" viewBox="0 0 34 36"><circle cx="17" cy="12" r="7" fill="none" stroke="var(--navy)" stroke-width="2"/><path d="M4 34c0-8 6-12 13-12s13 4 13 12z" fill="none" stroke="var(--navy)" stroke-width="2"/></svg></div>
  <h3>Customer Service</h3>
  <p>Need something out of the ordinary? Just ask us. Flexibility is engrained in our culture. Each member of our experienced staff</p>
</div>

<!-- welcome -->
<svg class="abs" style="left:0;top:1550px" width="1200" height="707" viewBox="0 0 1200 707" aria-hidden="true">
  <path d="M0 97 Q600 -100 1200 97 V707 H0Z" fill="var(--navy)"/>
</svg>
<h2 class="abs heading welcome-title">Welcome to Harborline</h2>

<div class="abs card" style="left:111px">
  <div class="card-photo" role="img" aria-label="Photo of hands using a calculator beside a laptop" style="background:linear-gradient(135deg,#4a3a2c,#a07850 60%,#2d3a52)"></div>
  <div class="card-icon"><svg width="32" height="30" viewBox="0 0 32 30"><rect x="3" y="4" width="20" height="14" rx="2" fill="none" stroke="#fff" stroke-width="2"/><path d="M7 9h12M12 26h16" stroke="#fff" stroke-width="2"/></svg></div>
  <h3 style="top:259px">Credit Application</h3>
  <p style="top:289px">Apply to become a client today</p>
  <a class="btn" style="left:84px;top:339px;width:141px">Apply online</a>
</div>
<div class="abs card" style="left:446px">
  <div class="card-photo" role="img" aria-label="Photo of a finger pressing an online registration key on a keyboard" style="background:linear-gradient(135deg,#6f747a,#c8ccd0 45%,#2f62b5 60%,#d0b8a4)"></div>
  <div class="card-icon"><svg width="30" height="30" viewBox="0 0 30 30"><rect x="4" y="3" width="22" height="17" rx="2" fill="none" stroke="#fff" stroke-width="2"/><path d="M11 12l3 3 5-6M10 27h10M15 20v7" stroke="#fff" stroke-width="2" fill="none"/></svg></div>
  <h3 style="top:250px">Registrations / Fhwa</h3>
  <p style="top:280px">Any time, any place, your registration and FHWA documents are here for you</p>
  <a class="btn" style="left:68px;top:346px;width:173px">Find registration</a>
</div>
<div class="abs card" style="left:780px">
  <div class="card-photo" role="img" aria-label="Photo of call center agents wearing headsets" style="background:linear-gradient(135deg,#c6ccd3,#e8e2da 50%,#6f7a86)"></div>
  <div class="card-icon"><svg width="30" height="30" viewBox="0 0 30 30"><path d="M5 16a10 10 0 0 1 20 0" fill="none" stroke="#fff" stroke-width="2"/><rect x="3" y="15" width="5" height="8" rx="2" fill="#fff"/><rect x="22" y="15" width="5" height="8" rx="2" fill="#fff"/></svg></div>
  <h3 style="top:259px">Request A Quote</h3>
  <p style="top:289px">Ready for a new lease on trailer leasing?</p>
  <a class="btn" style="left:84px;top:339px;width:141px">Get a quote</a>
</div>

<!-- info -->
<div class="abs" style="left:0;top:2256px;width:1200px;height:461px;background:var(--slate)"></div>
<svg class="abs" style="left:612px;top:2256px" width="588" height="482" viewBox="0 0 588 482" role="img" aria-label="Photo of a white leasing trailer on a city bridge">
  <defs>
    <linearGradient id="infoPhoto" x1="0" y1="0" x2="1" y2="1">
      <stop offset="0" stop-color="#aeb6be"/>
      <stop offset=".5" stop-color="#e4e6e8"/>
      <stop offset="1" stop-color="#50555a"/>
    </linearGradient>
  </defs>
  <path d="M0 461 Q60 80 200 0 H588 V482 H560 Q300 300 0 461Z" fill="url(#infoPhoto)"/>
  <path d="M120 461 Q60 200 260 80 Q430 10 588 40" fill="none" stroke="var(--slate)" stroke-width="34"/>
  <path d="M560 482 Q380 320 520 150" fill="none" stroke="var(--slate)" stroke-width="22"/>
</svg>

<h2 class="abs heading info-title">Looking for more<br>information?</h2>
<p class="abs info-sub">Fill in your details below for an information pack and discussion with one of our friendly affiliate managers</p>
<div class="abs field" style="left:113px;top:2480px">Your Name</div>
<div class="abs field" style="left:351px;top:2480px">Email Address</div>
<div class="abs field" style="left:113px;top:2533px">Your Phone Number</div>
<div class="abs field" style="left:351px;top:2533px">Location</div>
<a class="abs btn" style="left:113px;top:2605px;width:166px;height:47px;font-size:16px">Send message</a>

<!-- footer -->
<div class="abs brand" style="left:111px;top:2890px"><span class="brand-dot"></span>Harborline</div>

<div class="abs foot-h" style="left:374px;top:2810px">Our Office Address</div>
<svg class="abs" style="left:374px;top:2858px" width="13" height="13" viewBox="0 0 13 13"><path d="M2 0h3l1 3-2 1.5a8 8 0 0 0 4.5 4.5L10 7l3 1v3a2 2 0 0 1-2 2A11 11 0 0 1 0 2a2 2 0 0 1 2-2z" fill="var(--navy)"/></svg>
<div class="abs foot-label" style="left:397px;top:2856px">Phone</div>
<div class="abs foot-text" style="left:397px;top:2870px">+1 888-555-0142</div>
<svg class="abs" style="left:372px;top:2910px" width="15" height="11" viewBox="0 0 15 11"><rect width="15" height="11" rx="1" fill="var(--navy)"/><path d="M1 1l6.5 5L14 1" stroke="#fff" stroke-width="1.3" fill="none"/></svg>
<div class="abs foot-label" style="left:397px;top:2907px">Email</div>
<div class="abs foot-text" style="left:397px;top:2921px">hello@harborline-leasing.example</div>
<svg class="abs" style="left:375px;top:2956px" width="9" height="13" viewBox="0 0 9 13"><path d="M4.5 0A4.5 4.5 0 0 1 9 4.5C9 8 4.5 13 4.5 13S0 8 0 4.5A4.5 4.5 0 0 1 4.5 0z" fill="var(--navy)"/><circle cx="4.5" cy="4.5" r="1.7" fill="#fff"/></svg>
<div class="abs foot-label" style="left:397px;top:2955px">Location</div>
<div class="abs foot-text" style="left:397px;top:2969px;width:225px">6625 Lorem ipsum dolor sit amet, consectetur adipiscing elit,</div>

<div class="abs foot-h" style="left:650px;top:2810px">Company</div>
<div class="abs foot-links" style="left:650px;top:2851px">Rent/Lease/Buy<br>Trailers<br>Services<br>Company<br>Careers</div>

<div class="abs foot-h" style="left:787px;top:2811px;font-size:18px">Subscribe for Updates</div>
<div class="abs" style="left:790px;top:2859px;width:297px;height:45px;border-radius:23px;background:#f1f2f4;font-size:12px;color:#555;padding:16px 23px">Emaill Address</div>
<a class="abs btn" style="left:963px;top:2859px;width:124px;height:45px;border-radius:23px;font-size:17px;background:#1d7fd6;text-transform:uppercase">Submit</a>
<svg class="abs" style="left:787px;top:2932px" width="13" height="13" viewBox="0 0 13 13"><rect x="1" y="2" width="10" height="10" rx="1.5" fill="none" stroke="var(--navy)" stroke-width="1.5"/><path d="M3.5 6.5l2.5 2.5 6-7" stroke="var(--navy)" stroke-width="1.8" fill="none"/></svg>
<div class="abs" style="left:809px;top:2931px;font-size:13.5px;font-weight:500;color:var(--navy)">Yes, Please Contact me.</div>
<div class="abs social" style="left:787px;top:2969px"></div>
<div class="abs social" style="left:830px;top:2969px"></div>
<div class="abs social" style="left:872px;top:2969px"></div>

<div class="abs" style="left:111px;top:3029px;width:900px;border-top:1px dashed #999"></div>
<a class="abs" style="left:1007px;top:3020px;width:81px;height:19px;border-radius:10px;background:var(--slate);color:#fff;font-size:11px;font-weight:700;display:flex;align-items:center;justify-content:center;gap:4px">
  <svg width="9" height="9" viewBox="0 0 9 9"><path d="M4.5 0L9 5H6v4H3V5H0z" fill="#fff"/></svg>Go Up</a>

<div class="abs legal" style="left:111px">© 2022 Harborline Trailer Leasing | All Rights Reserved</div>
<div class="abs legal" style="left:760px">Privacy Policy &nbsp; | &nbsp; Cookie Policy &nbsp; | &nbsp; Terms Of Services</div>

</body>
</html>
```